Designs for a Barrister's chambers

Design stationery (including business card and letterhead) for a barrister's chambers -- similar to a law firm, using the enclosed logo. The current designs are not fit for purpose.

```html
<!DOCTYPE html>
<html lang="en">
<head>
<meta charset="utf-8">
<title>Marlowe Court Chambers – Stationery</title>
<link href="https://fonts.googleapis.com/css2?family=Figtree:wght@500;600;700&family=Roboto:wght@400;500&display=swap" rel="stylesheet">
<style>
  :root {
    --backdrop: #c6c6c6;
    --paper: #ffffff;
    --teal: #0e93b3;
    --navy: #0f1b2b;
    --card-dark: #111a24;
    --ink: #2b2b2b;
    --ink-soft: #555b61;
    --rule: #1a1a1a;
  }
  * { margin: 0; padding: 0; box-sizing: border-box; }
  html, body { width: 1200px; height: 900px; overflow: hidden; }
  body {
    background: var(--backdrop);
    position: relative;
    font-family: "Roboto", Arial, sans-serif;
    color: var(--ink);
  }
  .sheet, .card { position: absolute; background: var(--paper); overflow: hidden; }
  .brand-name {
    font-family: "Figtree", Arial, sans-serif;
    font-weight: 600;
    color: var(--navy);
    line-height: 1.02;
    letter-spacing: -0.2px;
    display: flex;
    align-items: center;
    white-space: nowrap;
  }
  .brand-mark { background: var(--teal); flex: none; }
  .pos { position: absolute; }

  /* Letterhead */
  .letterhead { left: 75px; top: 96px; width: 525px; height: 736px; }
  .letterhead .brand-name { left: 61px; top: 42px; font-size: 15.5px; gap: 8px; }
  .letterhead .brand-mark { width: 28px; height: 28px; }
  .letter-contact {
    right: 57px; top: 57px; text-align: right;
    font-size: 7.8px; line-height: 12.8px; color: var(--ink);
  }
  .letter-contact li { list-style: none; display: flex; justify-content: flex-end; align-items: center; gap: 5px; }
  .letter-contact svg { width: 8px; height: 8px; fill: var(--teal); }
  .recipient { left: 63px; top: 187px; font-size: 8px; }
  .recipient .name { font-size: 10.5px; margin-top: 4px; color: #111; }
  .recipient .role { font-size: 8px; color: var(--ink-soft); }
  .salutation { left: 63px; top: 243px; font-size: 8.5px; }
  .letter-date { right: 63px; top: 242px; font-size: 8.5px; }
  .letter-body { left: 63px; top: 289px; width: 400px; font-size: 8.3px; line-height: 15.4px; color: #3a3a3a; }
  .letter-body p + p { margin-top: 12px; }
  .sign-off { left: 63px; top: 547px; font-size: 8.3px; }
  .signatory { left: 63px; top: 576px; font-size: 10.5px; color: #111; }
  .signatory span { display: block; font-size: 8px; color: var(--ink-soft); }
  .band { position: absolute; left: 0; bottom: 0; }

  /* Business card front */
  .card-front { left: 657px; top: 179px; width: 460px; height: 262px; }
  .card-front .brand-name { left: 33px; top: 111px; font-size: 17.5px; gap: 7px; }
  .card-front .brand-mark { width: 34px; height: 34px; }
  .card-divider { left: 200px; top: 67px; width: 2px; height: 121px; background: var(--teal); }
  .holder { left: 219px; top: 64px; font-family: "Figtree", Arial, sans-serif; }
  .holder .name { font-size: 18px; font-weight: 700; color: var(--navy); }
  .holder .title { font-size: 13px; font-weight: 600; color: var(--teal); margin-top: 1px; }
  .card-contact { left: 219px; top: 122px; font-family: "Figtree", Arial, sans-serif; font-weight: 700; font-size: 9.5px; color: var(--navy); line-height: 11px; }
  .card-contact .row { display: flex; align-items: center; gap: 6px; margin-bottom: 5px; }
  .card-contact .icon { width: 11px; height: 11px; border-radius: 2px; background: var(--teal); display: flex; align-items: center; justify-content: center; flex: none; }
  .card-contact .icon.round { border-radius: 50%; }
  .card-contact svg { width: 7px; height: 7px; fill: #fff; }
  .card-address { right: 30px; bottom: 7px; font-family: "Figtree", Arial, sans-serif; font-weight: 600; font-size: 12px; color: #fff; }

  /* Business card back */
  .card-back { left: 658px; top: 482px; width: 460px; height: 263px; background: var(--card-dark); }
  .back-pattern { position: absolute; inset: 0; background: linear-gradient(135deg, #16212d 0%, #111a24 55%, #0e161f 100%); }
  .card-back .brand-name { left: 259px; top: 179px; font-size: 18px; color: #fff; gap: 8px; }
  .card-back .brand-mark { width: 38px; height: 38px; }
</style>
</head>
<body>

<section class="sheet letterhead" aria-label="Letterhead">
  <div class="pos brand-name"><span class="brand-mark"></span><span>Marlowe Court<br>Chambers</span></div>
  <ul class="pos letter-contact">
    <li>0200 000 1111 <svg viewBox="0 0 10 10"><path d="M2 1l2 2-1 1.3c.6 1.2 1.5 2.1 2.7 2.7L7 6l2 2-1.2 1.5C4.5 9.2.8 5.5.5 2.2z"/></svg></li>
    <li style="padding-right:13px">07000 111 222</li>
    <li>lionel.ashcombe@marlowecourtchambers.com <svg viewBox="0 0 10 10"><path d="M0 2h10v6H0zM0 2l5 3.5L10 2v1L5 6.5 0 3z"/></svg></li>
    <li>www.marlowecourtchambers.com <svg viewBox="0 0 10 10"><circle cx="5" cy="5" r="4.5"/></svg></li>
  </ul>

  <div class="pos recipient">To,<div class="name">Peter Holloway</div><div class="role">Managing Director</div></div>
  <div class="pos salutation">Dear</div>
  <div class="pos letter-date">Date: 20 March 2020</div>

  <div class="pos letter-body">
    <p>There are many variations of passages of Lorem Ipsum available, but the majority have suffered alteration in some form, by injected humour, or randomised words which don't look even slightly believable. If you are going to use a passage of Lorem Ipsum, you need to be sure there isn't anything embarrassing hidden in the middle of text tor on the Internet.</p>
    <p>Lorem Ipsum available, but the majority have suffered alteration in some form, by injected humour, or randised words which don't look even slightly believable. If you are going to use a passage of Lorem Ipsum, you need to be sure there isn't anything embarrassing hidden in the middle of text.</p>
    <p>It is a long established fact that a reader will be distracted by the readable content of a page when looking at its layout. The point of using Lorem Ipsum is that it has a more-or-less normal distribution of letters to using 'Content here, content here.</p>
    <p>But I must explain to you how all this mistaken idea of denouncing pleasure and praising pain was born and I will give you a complete account of the system.</p>
  </div>

  <div class="pos sign-off">Regards,</div>
  <div class="pos signatory">Daniel Reeve<span>Manager</span></div>

  <svg class="band" width="525" height="40" viewBox="0 0 525 40" aria-hidden="true">
    <polygon points="0,6 278,6 274,20 0,20" fill="var(--teal)"/>
    <rect x="0" y="25" width="272" height="3" fill="var(--rule)"/>
    <polygon points="283,0 525,0 525,40 273,40" fill="var(--teal)"/>
  </svg>
</section>

<section class="card card-front" aria-label="Business card, front">
  <div class="pos brand-name"><span class="brand-mark"></span><span>Marlowe Court<br>Chambers</span></div>
  <div class="pos card-divider"></div>
  <div class="pos holder"><div class="name">Lionel Ashcombe</div><div class="title">Barrister</div></div>
  <div class="pos card-contact">
    <div class="row"><span class="icon"><svg viewBox="0 0 10 10"><path d="M2 1l2 2-1 1.3c.6 1.2 1.5 2.1 2.7 2.7L7 6l2 2-1.2 1.5C4.5 9.2.8 5.5.5 2.2z"/></svg></span><span>0200 000 1111<br>07000 111 222</span></div>
    <div class="row" style="margin-top:8px"><span class="icon"><svg viewBox="0 0 10 10"><path d="M0 2h10v6H0zM0 2l5 3.5L10 2v1L5 6.5 0 3z" fill="#fff"/></svg></span><span>lionel.ashcombe@marlowecourtchambers.com</span></div>
    <div class="row"><span class="icon round"><svg viewBox="0 0 10 10"><circle cx="5" cy="5" r="3" fill="none" stroke="#fff" stroke-width="1.2"/></svg></span><span>www.marlowecourtchambers.com</span></div>
  </div>
  <svg class="band" width="460" height="26" viewBox="0 0 460 26" aria-hidden="true">
    <rect x="0" y="5" width="225" height="7" fill="var(--teal)"/>
    <rect x="0" y="16" width="222" height="3" fill="var(--rule)"/>
    <polygon points="223,0 460,0 460,26 216,26" fill="var(--teal)"/>
  </svg>
  <div class="pos card-address">42 Kestrel Lane, London EC1A 0ZZ</div>
</section>

<section class="card card-back" aria-label="Business card, back">
  <div class="back-pattern" role="img" aria-label="Subtle tone-on-tone repeating brand pattern across the dark card"></div>
  <div class="pos brand-name"><span class="brand-mark"></span><span>Marlowe Court<br>Chambers</span></div>
</section>

</body>
</html>
```